I need a business card for ALVA Holdings. We are a young startup based in New Zealand working in internet marketing and web development. The design should have some element connected to New Zealand, such as wave, koru or silver fern, just don't use a kiwi bird.

```html
<!DOCTYPE html>
<html lang="en">
<head>
<meta charset="utf-8">
<title>ALVA Holdings — Business Card</title>
<link rel="stylesheet" href="https://fonts.googleapis.com/css2?family=Lato:ital,wght@0,300;0,700;1,300&display=swap">
<style>
  :root {
    --blue: #1570b8;
    --orange: #f05a28;
    --white: #ffffff;
    --ink: #000000;
    --muted: #333333;
    --page: #ffffff;
  }
  * { margin: 0; padding: 0; box-sizing: border-box; }
  html, body {
    width: 1200px;
    height: 750px;
    overflow: hidden;
    background: var(--page);
  }
  .canvas {
    position: relative;
    width: 1200px;
    height: 750px;
    font-family: "Lato", sans-serif;
  }
  .card {
    position: absolute;
    width: 443px;
    height: 247px;
    overflow: hidden;
  }
  /* Front */
  .card-front {
    left: 134px;
    top: 252px;
    background: var(--blue);
  }
  .card-front .diagonal {
    position: absolute;
    inset: 0;
    width: 100%;
    height: 100%;
  }
  .brand-name {
    position: absolute;
    right: 26px;
    top: 40px;
    color: var(--white);
    font-weight: 700;
    font-size: 22px;
    letter-spacing: 2px;
    white-space: nowrap;
  }
  /* Back */
  .card-back {
    left: 623px;
    top: 253px;
    background: var(--white);
    border: 1px solid var(--ink);
  }
  .wave-panel {
    position: absolute;
    left: 0;
    top: 0;
    width: 210px;
    height: 245px;
  }
  .wave-line {
    fill: none;
    stroke: var(--white);
    stroke-linecap: round;
  }
  .contact {
    position: absolute;
    left: 229px;
    top: 47px;
  }
  .person-name {
    font-weight: 700;
    font-size: 26px;
    line-height: 27px;
    color: var(--ink);
  }
  .person-role {
    margin-top: 4px;
    font-weight: 300;
    font-size: 14px;
    color: var(--muted);
    letter-spacing: 0.5px;
  }
  .contact-details {
    margin-top: 39px;
    font-weight: 300;
    font-style: italic;
    font-size: 14px;
    line-height: 21px;
    color: var(--muted);
  }
</style>
</head>
<body>
<main class="canvas">
  <section class="card card-front" aria-label="Business card front">
    <svg class="diagonal" viewBox="0 0 472 264" preserveAspectRatio="none" aria-hidden="true">
      <polygon points="0,0 49,0 312,264 0,264" fill="var(--white)"/>
      <polygon points="0,0 27,0 290,264 0,264" fill="var(--orange)"/>
    </svg>
    <p class="brand-name">ALVA HOLDINGS</p>
  </section>

  <section class="card card-back" aria-label="Business card back">
    <svg class="wave-panel" viewBox="0 0 210 245" role="img" aria-label="Blue panel with ocean wave lines">
      <defs>
        <clipPath id="panel-shape">
          <path d="M0 0 H118 Q206 40 206 122 Q206 205 118 245 H0 Z"/>
        </clipPath>
      </defs>
      <path d="M0 0 H118 Q206 40 206 122 Q206 205 118 245 H0 Z" fill="var(--blue)"/>
      <g clip-path="url(#panel-shape)">
        <path class="wave-line" stroke-width="6" d="M-10 100 q25 -22 50 0 t50 0 t50 0 t50 0 t50 0"/>
        <path class="wave-line" stroke-width="6" d="M-10 135 q25 -22 50 0 t50 0 t50 0 t50 0 t50 0"/>
        <path class="wave-line" stroke-width="6" d="M-10 170 q25 -22 50 0 t50 0 t50 0 t50 0 t50 0"/>
      </g>
    </svg>
    <div class="contact">
      <h1 class="person-name">Rowan<br>Whitaker</h1>
      <p class="person-role">CEO</p>
      <p class="contact-details">
        r.whitaker@alvaholdings.com<br>
        (022) 4817-362
      </p>
    </div>
  </section>
</main>
</body>
</html>
```